Fairbrook's Vacation Rentals Business Card

Multi Million dollar villa rentals in the Dominican Republic.

Industry/Entity Type

Business

Contact Information for Business Card

I am looking for a high-end look around my company name/logo (see attached) on one side incorporating the following info: first and last name, title, address, phone #, email and company website. On the backside I want to add a full color picture of one of our villas (see attached).

```html
<!DOCTYPE html>
<html lang="en">
<head>
<meta charset="utf-8">
<title>Fairbrook's Vacation Rentals – Business Card</title>
<link href="https://fonts.googleapis.com/css2?family=Open+Sans:wght@400;600&display=swap" rel="stylesheet">
<style>
  :root {
    --page-bg: #e9e6e1;
    --card-bg: #ececec;
    --ink: #1f1f1f;
    --accent: #f0882a;
    --sky: #4f8fd8;
    --villa: #f1ede6;
    --roof: #c2643e;
    --pool: #1aa3e0;
    --shadow: rgba(0,0,0,0.18);
  }
  * { margin: 0; padding: 0; box-sizing: border-box; }
  html, body { width: 1200px; height: 900px; overflow: hidden; }
  body {
    background: var(--page-bg);
    font-family: "Open Sans", Arial, sans-serif;
    color: var(--ink);
    position: relative;
  }
  .card {
    position: absolute;
    width: 525px;
    height: 300px;
    top: 300px;
    box-shadow: 0 10px 24px var(--shadow);
    overflow: hidden;
  }
  .card--back { left: 50px; }
  .card--front { left: 625px; background: var(--card-bg); }

  .villa-photo {
    width: 100%;
    height: 100%;
    background:
      linear-gradient(180deg,
        var(--sky) 0%, #8fbde8 14%,
        var(--roof) 16%, var(--roof) 20%,
        var(--villa) 21%, #dcd6cc 58%,
        #6f7a5a 62%, #e9e4da 68%,
        #3a7bb8 74%, var(--pool) 80%, #0f86c8 100%);
  }

  .brand {
    position: absolute;
    left: 70px;
    top: 62px;
    display: flex;
    align-items: center;
    gap: 14px;
  }
  .brand__dot {
    width: 34px; height: 34px;
    border-radius: 50%;
    background: var(--accent);
  }
  .brand__name {
    font-weight: 600;
    font-size: 25px;
    color: var(--ink);
    letter-spacing: 0.2px;
  }

  .contact {
    position: absolute;
    left: 302px;
    top: 142px;
    list-style: none;
    font-size: 12.5px;
    line-height: 21px;
  }
  .contact li { display: flex; align-items: center; gap: 8px; }
  .contact svg { width: 10px; height: 10px; fill: var(--accent); flex: none; }

  .person {
    position: absolute;
    left: 110px;
    top: 185px;
    text-align: right;
    width: 170px;
  }
  .person__name { color: var(--accent); font-weight: 600; font-size: 16px; line-height: 20px; }
  .person__title { font-size: 13px; line-height: 18px; }

  .divider {
    position: absolute;
    left: 0; right: 0;
    top: 238px;
    height: 1px;
    background: var(--accent);
  }
  .address {
    position: absolute;
    left: 0; right: 0;
    top: 256px;
    text-align: center;
    font-size: 13.5px;
  }
</style>
</head>
<body>
  <section class="card card--back">
    <div class="villa-photo" role="img" aria-label="Photograph of a white two-storey villa with terracotta roof, arched terrace, palm trees and blue loungers beside a swimming pool"></div>
  </section>

  <section class="card card--front">
    <div class="brand">
      <span class="brand__dot"></span>
      <span class="brand__name">Fairbrook's Vacation Rentals</span>
    </div>

    <ul class="contact">
      <li><svg viewBox="0 0 10 10"><path d="M2 0.5 L4 2.5 L3 4 Q4.5 6 6 7 L7.5 6 L9.5 8 L8 9.5 Q3.5 9 0.5 2 Z"/></svg>(044)555019283</li>
      <li><svg viewBox="0 0 10 10"><path d="M0.5 2 H9.5 V8.5 H0.5 Z M0.8 2.3 L5 5.5 L9.2 2.3" stroke="#ececec" stroke-width="0.8"/></svg>info@fairbrookrentals.com</li>
      <li><svg viewBox="0 0 10 10"><circle cx="5" cy="5" r="4.6"/></svg>www.fairbrookrentals.com</li>
    </ul>

    <div class="person">
      <p class="person__name">Daniel Moreno</p>
      <p class="person__title">Managing Director</p>
    </div>

    <div class="divider"></div>
    <p class="address">18 Playa Serena, Dominican Republic, 23000</p>
  </section>
</body>
</html>
```